Velmora Solutions Website Design

We are a B2B startup offering a free virtual data room and deal management platform for small businesses. We need a 10-page website geared towards business executives and entrepreneurs that is simple, uploads quickly and provides a good introduction to our product. We've attached a document setting forth the text of 8 of the 10 pages (the other two - Resources and Blog - need to be designed to allow the future posting of white papers and blog entries) and links to the screenshots and GIFs, all of which are in a folder on dropbox. We've also attached a zip file with our logo and a pdf file with our font and colors. Examples of websites we like include www.tarnwick.example, www.plovebar.example and https://brimlo.example.

Target Market(s)

Small business owners, business executives and entrepreneurs

Industry/Entity Type

Finance

Coding

Coded - Design and coding required

Number of Pages Required

5+ page

Font styles to use
Sans Serif

Colors
85abd2
f9ba93

Requirements
Must have
• Please use the Wordpress kestle theme I uploaded to code the site.
Nice to have
• Clean, uncluttered design. White background. Screenshots and gifs should be shown on monitors (desktop, laptop and iPad only). Blue and orange are our corporate colors, but you’re not limited to those two colors. See uploaded logo guide for complementary colors or use your own judgment.

```html
<!DOCTYPE html>
<html lang="en">
<head>
<meta charset="utf-8">
<title>Velmora – Manage your workflow</title>
<link rel="stylesheet" href="https://fonts.googleapis.com/css2?family=Barlow:wght@400;500;600;700;800&display=swap">
<style>
:root{
  --bg:#f1f1f1;
  --ink:#2c2c2c;
  --text:#3a3a3a;
  --muted:#7d7d7d;
  --brand:#4a6b82;
  --accent:#e8742a;
  --green:#7a9a34;
  --plus:#3f6a8a;
  --line:#e3e3e3;
  --card:#ffffff;
}
*{margin:0;padding:0;box-sizing:border-box}
html,body{width:1200px;height:1198px;overflow:hidden}
body{background:var(--bg);font-family:"Barlow",sans-serif;color:var(--text);position:relative}
.abs{position:absolute}

/* header */
.logo{left:52px;top:28px;font-size:32px;font-weight:600;color:var(--brand);letter-spacing:-.5px;line-height:36px}
.nav{left:195px;top:38px;display:flex;gap:28px;font-size:15px;color:#4a4a4a}
.nav span.drop::after{content:"";display:inline-block;margin-left:7px;vertical-align:middle;border:3.5px solid transparent;border-top-color:#666;transform:translateY(2px)}
.cta{left:1039px;top:23px;width:136px;height:48px;background:var(--green);color:#fff;font-weight:700;font-size:14px;display:flex;align-items:center;justify-content:center;letter-spacing:.3px}

/* hero */
.hero-title{left:227px;top:170px;font-size:45px;line-height:45px;font-weight:700;color:var(--ink);letter-spacing:1px}
.hero-copy{left:225px;top:323px;width:300px;font-size:15px;line-height:17px;color:#333}
.watermark{left:945px;top:120px;font-size:104px;line-height:92px;font-weight:700;color:#fff;white-space:nowrap;letter-spacing:2px}

.laptop-screen{left:592px;top:155px;width:381px;height:243px;border:8px solid #e6e6e6;border-bottom:none;border-radius:10px 10px 0 0;background:#fff}
.laptop-base{left:563px;top:397px;width:440px;height:20px;background:#fff;border-radius:0 0 14px 14px;box-shadow:0 2px 4px rgba(0,0,0,.05)}
.screen-ui{left:600px;top:163px;width:365px;height:235px}

.share-card{left:644px;top:125px;width:276px;height:232px;background:var(--card);box-shadow:0 6px 22px rgba(0,0,0,.12);border-radius:3px}
.share-head{display:flex;justify-content:space-between;padding:14px 13px 0 15px;font-size:12px;color:#8a8a8a;height:33px}
.share-head em{font-style:normal;font-size:11px}
.share-row{height:34.5px;border-bottom:1.5px solid var(--line);display:flex;align-items:center;justify-content:space-between;padding:0 13px 0 17px;font-size:14px;color:#333}
.plus{width:14px;height:14px;border-radius:50%;background:var(--plus);position:relative}
.plus::before,.plus::after{content:"";position:absolute;background:#fff;left:3px;top:6.25px;width:8px;height:1.5px}
.plus::after{transform:rotate(90deg)}
.pager{position:absolute;left:19px;top:190px;display:flex;gap:7px}
.pager b{width:26px;height:26px;border-radius:50%;background:#e8e8e8;font-size:11px;font-weight:600;color:#444;display:flex;align-items:center;justify-content:center}
.pager b.on{background:var(--green);color:#fff}
.next{position:absolute;left:190px;top:190px;width:73px;height:26px;border-radius:13px;background:#c9c9c9;color:#fff;font-size:11px;font-weight:600;display:flex;align-items:center;justify-content:center;gap:4px}
.play{left:753px;top:214px;width:60px;height:60px;border-radius:50%;background:#fff;box-shadow:0 3px 12px rgba(0,0,0,.15)}

.dots{display:flex;flex-direction:column;gap:21.5px}
.dots i{width:7px;height:7px;border-radius:50%;background:#cfcfcf;display:block}
.dots i.on{background:#555}

/* intro features */
.love-label{left:228px;top:443px;font-size:10.5px;font-weight:700;color:#333;letter-spacing:.2px}
.perk{top:468px;display:flex;gap:16px;align-items:flex-start;font-size:15px;line-height:16.5px;color:#333}

/* quote */
.quote{left:43px;top:618px;width:210px;font-size:22.5px;line-height:28.5px;font-weight:700;color:#fff}
.quote-by{left:43px;top:796px;width:210px;font-size:15px;line-height:20px;font-weight:600;color:#c4c4c4}

/* features grid */
.features-title{left:0;width:1200px;top:658px;text-align:center;font-size:45px;line-height:45px;font-weight:700;color:var(--ink);letter-spacing:1px}
.features-sub{left:0;width:1200px;top:757px;text-align:center;font-size:15.5px;line-height:17px;color:#333}
.feature{width:220px;text-align:center}
.feature svg{display:block;margin:0 auto}
.feature h3{font-size:18.5px;font-weight:500;color:#333;margin-top:12px;line-height:20px}
.feature p{font-size:13px;line-height:15px;color:#666;margin-top:7px}
</style>
</head>
<body>

<header>
  <div class="abs logo">Velmora</div>
  <nav class="abs nav">
    <span class="drop">Features</span><span>Customers</span><span class="drop">Company</span><span>Contact</span>
  </nav>
  <div class="abs cta">TRY IT NOW</div>
</header>

<section class="hero">
  <h1 class="abs hero-title">MANAGE YOUR<br>WORKFLOW<br>BETTER WITH</h1>
  <p class="abs hero-copy">The Velmora assistant is a secure, sharable workflow management platform designed with your needs in mind.</p>

  <div class="abs watermark">WORK<br>FLOW</div>

  <div class="abs laptop-screen"></div>
  <svg class="abs screen-ui" viewBox="0 0 365 235" aria-hidden="true">
    <rect x="10" y="8" width="60" height="14" rx="7" fill="#f3f3f3"/>
    <circle cx="18" cy="15" r="4" fill="#4a6b82"/>
    <text x="10" y="44" font-family="Barlow,sans-serif" font-size="12" font-weight="600" fill="#4a6b82">Velmora</text>
    <rect x="10" y="58" width="40" height="7" fill="#f0f0f0"/>
    <rect x="10" y="72" width="45" height="7" fill="#f0f0f0"/>
    <g fill="#dcdcdc"><rect x="12" y="90" width="30" height="3"/><rect x="12" y="100" width="26" height="2"/><rect x="12" y="110" width="34" height="2"/><rect x="12" y="120" width="38" height="2"/><rect x="12" y="130" width="28" height="2"/><rect x="12" y="140" width="30" height="2"/><rect x="12" y="150" width="32" height="2"/></g>
    <rect x="300" y="40" width="8" height="8" rx="4" fill="#e8e8e8"/>
    <text x="312" y="47" font-family="Barlow,sans-serif" font-size="5" fill="#777">Dana Pell</text>
    <circle cx="306" cy="64" r="4" fill="#7a9a34"/><circle cx="331" cy="80" r="4" fill="#e8742a"/>
    <g fill="#e2e2e2"><rect x="300" y="92" width="45" height="2"/><rect x="300" y="104" width="40" height="2"/><rect x="300" y="116" width="44" height="2"/><rect x="300" y="128" width="36" height="2"/><rect x="300" y="140" width="42" height="2"/><rect x="300" y="152" width="38" height="2"/><rect x="300" y="164" width="44" height="2"/><rect x="300" y="176" width="40" height="2"/><rect x="300" y="188" width="36" height="2"/></g>
    <rect x="234" y="200" width="120" height="30" fill="none" stroke="#eee"/>
    <rect x="68" y="200" width="110" height="30" fill="none" stroke="#eee"/>
  </svg>
  <div class="abs laptop-base"></div>

  <div class="abs share-card">
    <div class="share-head"><span>What do you want to share?</span><em>✓ Select all</em></div>
    <div class="share-row"><span>Credit app</span><i class="plus"></i></div>
    <div class="share-row"><span>Legal documents</span><i class="plus"></i></div>
    <div class="share-row"><span>Due diligence</span><i class="plus"></i></div>
    <div class="share-row"><span>Working group</span><i class="plus"></i></div>
    <div class="pager"><b class="on">1</b><b>2</b><b>3</b></div>
    <div class="next">→ Next</div>
  </div>
  <div class="abs play">
    <svg width="60" height="60" viewBox="0 0 60 60" aria-hidden="true"><path d="M25 20 L40 30 L25 40 Z" fill="#3f6a8a"/></svg>
  </div>

  <div class="abs dots" style="left:1139px;top:211px"><i class="on"></i><i></i><i></i><i></i><i></i><i></i><i></i></div>

  <div class="abs love-label">HERE ARE SOME FEATURES YOU'LL LOVE:</div>
  <div class="abs perk" style="left:225px">
    <svg width="32" height="28" viewBox="0 0 32 28" aria-hidden="true"><g fill="#e8742a"><circle cx="10" cy="8" r="5"/><circle cx="22" cy="9" r="4.5"/><path d="M0 26c0-7 4-10 10-10s10 3 10 10z"/><path d="M18 26c0-5 2-8 6-8s8 3 8 8z"/></g></svg>
    <span>Built for internal<br>and external collaboration</span>
  </div>
  <div class="abs perk" style="left:499px">
    <svg width="32" height="34" viewBox="0 0 32 34" aria-hidden="true"><path d="M0 2h32v24H10l-8 7v-7H0z" fill="#e8742a"/><path d="M8 20l3-6 9-9 3 3-9 9z M8 21h16" stroke="#fff" stroke-width="2" fill="none"/></svg>
    <span>Highly intuitive<br>and customizable</span>
  </div>
  <div class="abs perk" style="left:721px">
    <svg width="30" height="32" viewBox="0 0 30 32" aria-hidden="true"><g stroke="#e8742a" stroke-width="3" fill="none"><path d="M20 8c-2-2-9-3-9 2s10 3 10 9-8 5-11 2"/><path d="M15 2v5M15 26v5"/><path d="M4 4l22 25"/></g></svg>
    <span>Free to use – no setup<br>or monthly fees</span>
  </div>
</section>

<section class="glance">
  <blockquote class="abs quote">"Efficient workflow management has resulted in an 85% savings in deal closings over the past six years."</blockquote>
  <div class="abs quote-by">The Global Council for Contract Practice</div>

  <h2 class="abs features-title">FEATURES<br>AT-A-GLANCE</h2>
  <p class="abs features-sub">User-friendly workflow management<br>software that saves time and money</p>

  <div class="abs dots" style="left:1139px;top:811px"><i></i><i class="on"></i><i></i><i></i><i></i><i></i><i></i></div>

  <div class="abs feature" style="left:225px;top:828px">
    <svg width="44" height="56" viewBox="0 0 44 56" aria-hidden="true"><g fill="none" stroke="#2f4b5e" stroke-width="2"><rect x="2" y="6" width="40" height="48" rx="2"/><rect x="7" y="11" width="30" height="38"/><rect x="16" y="2" width="12" height="7"/><rect x="18" y="16" width="8" height="6"/><path d="M22 22v5M13 27h18M13 27v5M22 27v5M31 27v5"/><rect x="10" y="32" width="6" height="5"/><rect x="19" y="32" width="6" height="5"/><rect x="28" y="32" width="6" height="5"/></g></svg>
    <h3>Workflow Management</h3>
    <p>Efficiently handle multi-party transactions with customizable, collaborative workflow software.</p>
  </div>
  <div class="abs feature" style="left:488px;top:828px">
    <svg width="48" height="56" viewBox="0 0 48 56" aria-hidden="true"><g fill="none" stroke="#2f4b5e" stroke-width="2"><rect x="2" y="5" width="44" height="49" rx="2"/><rect x="17" y="1" width="14" height="7"/><path d="M8 17l3 3 5-6M8 29l3 3 5-6"/><rect x="8" y="38" width="6" height="5"/><path d="M20 18h20M20 30h20M20 41h20M20 24h14M20 36h14"/></g></svg>
    <h3>Built-in Checklists</h3>
    <p>Swap old-process checklists for online linked to documents hosted</p>
  </div>
  <div class="abs feature" style="left:752px;top:826px">
    <svg width="58" height="58" viewBox="0 0 58 58" aria-hidden="true"><g fill="none" stroke="#2f4b5e" stroke-width="2"><circle cx="29" cy="29" r="6"/><circle cx="51" cy="7" r="5"/><circle cx="7" cy="51" r="5"/><circle cx="29" cy="53" r="4"/><circle cx="11" cy="11" r="3"/><circle cx="51" cy="47" r="3"/><path d="M33 25l14-14M25 33l-14 14M29 35v14M25 25l-12-12M33 33l16 12"/></g></svg>
    <h3>Real-time Sharing</h3>
    <p>Automate new file requests and enable real-time downloads from a single self-service portal.</p>
  </div>

  <div class="abs feature" style="left:225px;top:988px">
    <svg width="56" height="56" viewBox="0 0 56 56" aria-hidden="true"><g fill="none" stroke="#2f4b5e" stroke-width="2"><circle cx="22" cy="22" r="18"/><circle cx="22" cy="22" r="12"/><path d="M35 35l16 16" stroke-width="4"/></g></svg>
    <h3>Better Transparency</h3>
    <p>Make all of your files visible to your partners in one place.</p>
  </div>
  <div class="abs feature" style="left:488px;top:988px">
    <svg width="56" height="56" viewBox="0 0 56 56" aria-hidden="true"><g fill="none" stroke="#2f4b5e" stroke-width="2"><path d="M6 2l4 3 4-3 4 3 4-3 4 3 4-3v50H6z"/><path d="M11 14h18M11 20h18M11 26h12"/><rect x="20" y="30" width="32" height="22"/><path d="M20 37h32M20 44h32M30 30v22M41 30v22"/></g></svg>
    <h3>Lower Costs</h3>
    <p>Share your files from anywhere with no setup or monthly fees.</p>
  </div>
  <div class="abs feature" style="left:752px;top:988px">
    <svg width="56" height="56" viewBox="0 0 56 56" aria-hidden="true"><g fill="none" stroke="#2f4b5e" stroke-width="2"><rect x="4" y="18" width="48" height="34" rx="2"/><circle cx="28" cy="10" r="7"/><path d="M28 17v14M24 28h4M24 24h4"/><path d="M10 26h10M10 32h10M36 26h10M36 32h10"/></g></svg>
    <h3>Enhanced Security</h3>
    <p>Host your data on encrypted Corvane Cloud servers with full audit trails.</p>
  </div>
</section>

</body>
</html>
```